Need Catering Menu designed - design that we want is attached

Hi,
We need a new catering menu designed for our cafe.
I have attached our coffee menu, we would like it to follow the same kind of layout.
It needs to be A4, and can be double sided.
I have attached a word doc of our catering menu, so this is what needs to be on the catering menu you produce.
Also, our contact details need to be on both sides of the menu:
Visit us instore to discuss catering options, or call 0438 672 914 or email marla@tevrostudio.com.au
I have also attached our new logo which I'd like incorporated into the menu
Target Market(s)
Doctors/Nurses
Hospital staff
University Students
Industry/Entity Type
Catering
Look and feel

```html
<!DOCTYPE html>
<html lang="en">
<head>
<meta charset="utf-8">
<title>Ward Nine – Catering Menus</title>
<link rel="stylesheet" href="https://fonts.googleapis.com/css2?family=Courier+Prime:ital,wght@0,400;1,400&family=Cutive&family=Oswald:wght@500&display=swap">
<style>
  :root {
    --backdrop: #a9653a;
    --board: #1d1d1d;
    --board-light: #2a2a2a;
    --chalk: #ececec;
    --chalk-soft: #d6d6d6;
    --brand-yellow: #f6f3a2;
  }
  * { margin: 0; padding: 0; box-sizing: border-box; }
  html, body { width: 1200px; height: 750px; overflow: hidden; }
  body { background: var(--backdrop); position: relative; }

  .menu-card {
    position: absolute;
    top: 65px;
    width: 436px;
    height: 617px;
    background: radial-gradient(ellipse at 50% 40%, var(--board-light), var(--board) 75%);
    color: var(--chalk);
  }
  .menu-card--tea { left: 107px; }
  .menu-card--breakfast { left: 647px; }

  .brand {
    position: absolute;
    top: 46px; left: 0; right: 0;
    display: flex; justify-content: center; align-items: center; gap: 12px;
  }
  .brand__mark { width: 40px; height: 40px; background: var(--brand-yellow); }
  .brand__name {
    font-family: 'Cutive', serif;
    font-size: 22px;
    color: var(--chalk);
    letter-spacing: 1px;
  }

  .tagline {
    position: absolute;
    top: 123px; left: 0; right: 0;
    text-align: center;
    font-family: 'Cutive', serif;
    font-size: 15px;
    color: var(--chalk);
  }

  .menu-panel {
    position: absolute;
    top: 179px; left: 29px;
    width: 379px; height: 369px;
    border: 2px solid var(--chalk);
    padding: 34px 8px 0 8px;
  }
  .menu-card--breakfast .menu-panel { top: 178px; left: 43px; width: 350px; padding-left: 9px; padding-right: 20px; }

  .ribbon {
    position: absolute;
    top: -24px; left: 27px;
    width: 325px; height: 43px;
  }
  .menu-card--breakfast .ribbon { left: 54px; width: 243px; }
  .ribbon svg { position: absolute; inset: 0; width: 100%; height: 100%; }
  .ribbon__title {
    position: relative;
    display: flex; align-items: center; justify-content: center;
    height: 100%;
    font-family: 'Oswald', sans-serif;
    font-weight: 500;
    font-size: 22px;
    color: #fff;
    letter-spacing: 0.2px;
  }

  .menu-list { list-style: none; font-family: 'Courier Prime', monospace; font-size: 13.5px; }
  .menu-item { display: flex; line-height: 25px; white-space: nowrap; }
  .menu-item__leader { flex: 1; overflow: hidden; margin: 0 2px; }
  .menu-item__leader::after { content: "...................................................................."; }
  .menu-item__price { min-width: 22px; }

  .menu-notes {
    margin-top: 28px;
    font-family: 'Courier Prime', monospace;
    font-style: italic;
    font-size: 11px;
    line-height: 14px;
    color: var(--chalk-soft);
  }
  .menu-notes p { margin-bottom: 14px; padding-left: 12px; text-indent: -12px; }

  .contact {
    position: absolute;
    top: 558px; left: 0; right: 0;
    text-align: center;
    font-family: 'Courier Prime', monospace;
    font-size: 11.5px;
    line-height: 16px;
    color: var(--chalk-soft);
  }
</style>
</head>
<body>

<section class="menu-card menu-card--tea">
  <div class="brand"><span class="brand__mark"></span><span class="brand__name">WARD NINE</span></div>
  <p class="tagline">coffee • catering • food to go</p>
  <div class="menu-panel">
    <div class="ribbon">
      <svg viewBox="0 0 325 43" preserveAspectRatio="none"><polygon points="1,1 324,1 311,21.5 324,42 1,42 14,21.5" fill="#1f1f1f" stroke="#ececec" stroke-width="2"/></svg>
      <h2 class="ribbon__title">MORNING and AFTERNOON TEA</h2>
    </div>
    <ul class="menu-list">
      <li class="menu-item"><span>Fruit Platter</span><span class="menu-item__leader"></span><span class="menu-item__price">$15</span></li>
      <li class="menu-item"><span>Muffin</span><span class="menu-item__leader"></span><span class="menu-item__price">$4.5</span></li>
      <li class="menu-item"><span>Mini Muffin</span><span class="menu-item__leader"></span><span class="menu-item__price">$2.5</span></li>
      <li class="menu-item"><span>Assorted Slices</span><span class="menu-item__leader"></span><span class="menu-item__price">$4</span></li>
      <li class="menu-item"><span>Assorted Cookies from</span><span class="menu-item__leader"></span><span class="menu-item__price">$3</span></li>
      <li class="menu-item"><span>Assorted Yoghurts</span><span class="menu-item__leader"></span><span class="menu-item__price">$5.5</span></li>
      <li class="menu-item"><span>Chia Pudding</span><span class="menu-item__leader"></span><span class="menu-item__price">$5.5</span></li>
      <li class="menu-item"><span>Banana Bread</span><span class="menu-item__leader"></span><span class="menu-item__price">$4.5</span></li>
      <li class="menu-item"><span>Juice</span><span class="menu-item__leader"></span><span class="menu-item__price">$8</span></li>
    </ul>
    <div class="menu-notes">
      <p>* Cups/Plates/Serviettes can be provided at a charge of $1 per person</p>
      <p>* Barista made coffee available</p>
    </div>
  </div>
  <div class="contact">
    Visit us instore to discuss catering options<br>
    call 0438 672 914<br>
    email marla@tevrostudio.com.au
  </div>
</section>

<section class="menu-card menu-card--breakfast">
  <div class="brand"><span class="brand__mark"></span><span class="brand__name">WARD NINE</span></div>
  <p class="tagline">coffee • catering • food to go</p>
  <div class="menu-panel">
    <div class="ribbon">
      <svg viewBox="0 0 243 43" preserveAspectRatio="none"><polygon points="1,1 242,1 229,21.5 242,42 1,42 14,21.5" fill="#1f1f1f" stroke="#ececec" stroke-width="2"/></svg>
      <h2 class="ribbon__title">BREAKFAST</h2>
    </div>
    <ul class="menu-list">
      <li class="menu-item"><span>Fruit Platter</span><span class="menu-item__leader"></span><span class="menu-item__price">$15</span></li>
      <li class="menu-item"><span>Bacon Egg and Cheese Roll</span><span class="menu-item__leader"></span><span class="menu-item__price">$6.5</span></li>
      <li class="menu-item"><span>Vegetarian Brekky Wrap</span><span class="menu-item__leader"></span><span class="menu-item__price">$6.5</span></li>
      <li class="menu-item"><span>Ham and Cheese Croissant</span><span class="menu-item__leader"></span><span class="menu-item__price">$6</span></li>
      <li class="menu-item"><span>Cheese and Tomato Croissant</span><span class="menu-item__leader"></span><span class="menu-item__price">$5.5</span></li>
      <li class="menu-item"><span>Ham and Cheese French Toast</span><span class="menu-item__leader"></span><span class="menu-item__price">$6.5</span></li>
      <li class="menu-item"><span>Assorted Yoghurts</span><span class="menu-item__leader"></span><span class="menu-item__price">$5.5</span></li>
      <li class="menu-item"><span>Bircher Muesli</span><span class="menu-item__leader"></span><span class="menu-item__price">$5.5</span></li>
      <li class="menu-item"><span>Chia Pudding</span><span class="menu-item__leader"></span><span class="menu-item__price">$5.5</span></li>
      <li class="menu-item"><span>Granola and Yoghurt</span><span class="menu-item__leader"></span><span class="menu-item__price">$5.5</span></li>
      <li class="menu-item"><span>Muffin</span><span class="menu-item__leader"></span><span class="menu-item__price">$4.5</span></li>
      <li class="menu-item"><span>Mini Muffin</span><span class="menu-item__leader"></span><span class="menu-item__price">$2.5</span></li>
      <li class="menu-item"><span>Juice</span><span class="menu-item__leader"></span><span class="menu-item__price">$8</span></li>
    </ul>
  </div>
  <div class="contact">
    Visit us instore to discuss catering options<br>
    call 0438 672 914<br>
    email marla@tevrostudio.com.au
  </div>
</section>

</body>
</html>
```